Existing Website Requiring new Pages

I have an existing word press website that was built using elementor.
Website: www.tallowmerecare.com.au
I require the Vacancies page (https://www.tallowmerecare.com.au/vacancies/) to be modified to display our new properties along with minor tweaks to how the information is presented.
The vacancies to be displayed are the exactly the same as those that are located on the homepage of QPD website (https://qpd.org.au/)
The new pages that link off the Vacancies tab will require custom design.
There are roughly 8 pages/properties to be incorporated. i wish for the design to be very similar to that displayed in the following link; https://www.solquarn.com.au/vacancies/merrylands
Along with this the back end has not been updated for the last 3 years so it also requires some maintenance.
Website is in the disability industry and the custom pages will display information relative to Property Vacancies.
I have attached a ZIP file with some design guides, the information for each of the properties (which will need to be modified to show our business name Tallowmere Healthcare) and the example of how it is to look based off the Solquarn website.
If you guys have any suggestions or ideas on how to make this more presentable or possible i'm open to your ideas.
Target Market(s)
People looking for SDA properties custom built for people with a disability
Industry/Entity Type
Disability
Coding
Coded - Design and coding required
Number of Pages Required
5+ page
Look and feel
Each slider illustrates characteristics of the customer's brand and the style your logo design should communicate.

```html
<!DOCTYPE html>
<html lang="en">
<head>
<meta charset="utf-8">
<title>Vacancies | Tallowmere Healthcare</title>
<link href="https://fonts.googleapis.com/css2?family=Montserrat:wght@400;500;600;700;800&display=swap" rel="stylesheet">
<style>
:root{
  --ink:#111;
  --accent:#d65f38;
  --accent-soft:#f29c78;
  --muted:#8c8c8c;
  --rule:#e4e4e4;
  --blue:#2a7fd0;
  --dark:#222;
  --bg:#fff;
}
*{margin:0;padding:0;box-sizing:border-box}
html,body{width:793px;height:1200px;overflow:hidden;background:var(--bg);font-family:"Montserrat",sans-serif;color:var(--ink)}
.page{position:relative;width:793px;height:1200px}
.abs{position:absolute}
.brand{display:flex;align-items:center;gap:5px;font-weight:700;color:#5a4a8a;letter-spacing:.5px;line-height:1.05}
.brand .dot{width:12px;height:12px;border-radius:50%;background:#e9468f;flex:none}
.header-brand{left:74px;top:28px;font-size:11px}
.nav{left:0;top:36px;width:793px;height:14px;font-size:8.5px;font-weight:600}
.nav span{position:absolute;top:0;white-space:nowrap}
.nav .active{color:var(--accent-soft)}
.hero{left:0;top:83px;width:793px;height:312px;background:linear-gradient(100deg,#c9b46a 0%,#8ea04e 35%,#6f8a45 60%,#9aa07a 80%,#7a7f6e 100%)}
.hero-title{left:91px;top:200px;font-size:40px;font-weight:800;color:#fff;letter-spacing:-.5px}
.card{position:absolute;width:150px;height:205px;background:#fff;border-radius:5px;box-shadow:0 2px 10px rgba(0,0,0,.12);overflow:hidden;text-align:center}
.card .photo{height:149px}
.card h3{margin-top:13px;font-size:11px;font-weight:600;color:var(--accent);letter-spacing:.3px}
.card p{margin-top:5px;font-size:10px;color:#222}
.divider{left:39px;top:945px;width:754px;height:1px;background:#efefef}
.footer-brand{left:78px;top:1005px;font-size:16px}
.contact{left:76px;top:1083px;font-size:8.5px;color:var(--muted);line-height:15px}
.contact li{list-style:none;display:flex;align-items:center;gap:6px}
.contact svg{width:10px;height:10px;flex:none}
.social{left:357px;top:983px;width:22px}
.social i{display:block;width:22px;height:22px;border-radius:50%;margin-bottom:6.5px}
.col{width:156px}
.col h4{font-size:10px;font-weight:500;letter-spacing:.4px;border-left:2px solid var(--blue);padding-left:9px;line-height:11px;margin-bottom:6px}
.col ul{list-style:none;border-top:1px solid var(--rule)}
.col li{font-size:8.5px;color:var(--muted);border-bottom:1px solid var(--rule);padding:5px 0 5px;line-height:15px}
.col-accom{left:420px;top:977px}
.col-what{left:592px;top:977px}
.col-what li{padding:3px 0 3px;line-height:16px}
.tag{left:773px;top:1139px;font-size:7px}
.bottom{left:0;top:1153px;width:793px;height:47px;background:var(--dark);color:#ccc;font-size:7.3px;text-align:center;line-height:47px}
.totop{left:750px;top:1167px;width:23px;height:23px;background:#111;display:flex;align-items:center;justify-content:center}
</style>
</head>
<body>
<div class="page">
  <div class="abs brand header-brand"><span class="dot"></span><span>TALLOWMERE<br>HEALTHCARE</span></div>
  <nav class="abs nav">
    <span style="left:292px">HOME</span>
    <span style="left:346px">ABOUT US</span>
    <span class="active" style="left:419px">WHAT WE DO <svg width="7" height="5" viewBox="0 0 7 5"><path d="M.5.5 3.5 4 6.5.5" fill="none" stroke="#f29c78" stroke-width="1"/></svg></span>
    <span style="left:507px">REFERRALS</span>
    <span style="left:587px">FEEDBACK</span>
    <span style="left:662px">CONTACT US</span>
  </nav>

  <div class="abs hero" role="img" aria-label="Carer pushing an elderly woman in a wheelchair along a sunlit country path"></div>
  <h1 class="abs hero-title">VACANCIES</h1>

  <div class="card" style="left:74px;top:459px"><div class="photo" role="img" aria-label="Modern grey house with garage" style="background:linear-gradient(#cfd6e0,#8c8478 60%,#6f8a4a)"></div><h3>PENRITH</h3><p>4 Bedroom SIL Home</p></div>
  <div class="card" style="left:238px;top:459px"><div class="photo" role="img" aria-label="Brick home with paved driveway" style="background:linear-gradient(#9fbbd8,#a0564a 45%,#5f8a3e 60%,#c58068)"></div><h3>MOUNT DRUITT</h3><p>4 Bedroom SIL Home</p></div>
  <div class="card" style="left:404px;top:459px"><div class="photo" role="img" aria-label="Cream brick single-storey house" style="background:linear-gradient(#5fa3e0,#e2d7a6 55%,#3e6e2e 75%,#9aa66a)"></div><h3>CASULA</h3><p>4 Bedroom SIL Home</p></div>
  <div class="card" style="left:569px;top:459px"><div class="photo" role="img" aria-label="Federation style cottage with shutters" style="background:linear-gradient(#8cbbe6,#e6d8c2 45%,#c9b8a0 70%,#5f9a3a)"></div><h3>EASTWOOD</h3><p>4 Bedroom SIL Home</p></div>

  <div class="card" style="left:74px;top:709px"><div class="photo" role="img" aria-label="Brick home with palm tree and lawn" style="background:linear-gradient(#8fc0ec,#c4a88e 50%,#4f9a34)"></div><h3>BAULKHAM HILLS</h3><p>4 Bedroom SIL Home</p></div>
  <div class="card" style="left:238px;top:709px"><div class="photo" role="img" aria-label="Orange brick house with long driveway" style="background:linear-gradient(#6fa8e4,#c46a3e 45%,#5d9a3a 65%,#b8b8b0)"></div><h3>MERRYLANDS</h3><p>4 Bedroom SIL Home</p></div>
  <div class="card" style="left:404px;top:709px"><div class="photo" role="img" aria-label="Apartment building beside a paved square" style="background:linear-gradient(#3f6f9a,#c0906a 50%,#8a5a48)"></div><h3>FAIRFIELD</h3><p>4 Bedroom SIL Home</p></div>
  <div class="card" style="left:569px;top:709px"><div class="photo" role="img" aria-label="Two-storey rendered house with bay windows" style="background:linear-gradient(#aab4bc,#d8d8d4 50%,#3d5a34)"></div><h3>LIVERPOOL</h3><p>4 Bedroom SIL Home</p></div>

  <div class="abs divider"></div>

  <div class="abs brand footer-brand"><span class="dot"></span><span>TALLOWMERE<br>HEALTHCARE</span></div>
  <ul class="abs contact">
    <li><svg viewBox="0 0 10 10"><rect x=".7" y="1.7" width="8.6" height="6.6" fill="none" stroke="#e9468f"/><path d="M.7 2 5 5.5 9.3 2" fill="none" stroke="#e9468f"/></svg>Email: info@tallowmerecare.com.au</li>
    <li><svg viewBox="0 0 10 10"><path d="M2 1 4 3 3 4.5C4 6 5 7 6.5 7L8 6 9.5 8 8 9.5C4 9 1 6 .5 2Z" fill="#e9468f"/></svg>Phone: +61 0491 570 156</li>
    <li><svg viewBox="0 0 10 10"><circle cx="5" cy="5" r="4.2" fill="none" stroke="#e9468f"/><path d="M5 2.5V5L6.8 6" fill="none" stroke="#e9468f"/></svg>Operating Hours: 9AM To 5PM Monday - Friday</li>
  </ul>
  <div class="abs social">
    <i style="background:#6b2c8a"></i>
    <i style="background:#2b62b8"></i>
    <i style="background:#222"></i>
    <i style="background:#1f7bbf"></i>
  </div>

  <div class="abs col col-accom">
    <h4>ACCOMMODATION</h4>
    <ul>
      <li>Supported Independent Living (SIL)</li>
      <li>Specialist Disability Accommodation (SDA)</li>
      <li>Short term Accommodation (Respite)</li>
      <li>Vacancies</li>
    </ul>
  </div>
  <div class="abs col col-what">
    <h4>WHAT WE DO</h4>
    <ul>
      <li>In Home Care</li>
      <li>Social &amp; Community Services</li>
      <li>Therapeutic Supports</li>
      <li>Support Coordination</li>
      <li>Home Modifications</li>
    </ul>
  </div>

  <div class="abs tag">C73</div>
  <div class="abs bottom">© Copyright 2024 | Tallowmere Healthcare | All Rights Reserved.</div>
  <div class="abs totop"><svg width="8" height="5" viewBox="0 0 8 5"><path d="M0 5 4 0 8 5Z" fill="#fff"/></svg></div>
</div>
</body>
</html>
```